New Company Website

Need a new website for my company Loxley Greenery.
Loxley Greenery offers four business lines: Interior Landscaping, Urbanscaping, Holiday Decorating, and Rental Plants.
Interior Landscaping is the interior installation and maintenance of live plants and flowers in corporate offices. Interiorscape contracts will be for a variety of terms from month to month to 3 years with differing price points in each option.
Urbanscaping refers to landscaping in the urban environment and is restricted in this definition to street side planters and medians, monument plantings and rooftop/balcony gardens.
Holiday Decorating is the Christmas/Hanukkah decorating during the winter season for corporate offices. The model for this business is to lease decorations for a period of 3 years.
Plant rentals is the short term rental of plants and live flowers (orchids, kalanchoe, etc) to event venues. The long term plan is to become the exclusive interior plant vendor for tradeshow organizations in the Tri-State area.

Target Market(s)

Office Managers, Building Managers, Event Coordinators

Industry/Entity Type

Landscaping

Requirements
Must have
• I love my logo. Please incorporate and use colors. Do not change logo.
Nice to have
• These are my competitors:
www.fernhollowdecor.com
www.qorvel.com

```html
<!DOCTYPE html>
<html lang="en">
<head>
<meta charset="utf-8">
<title>Loxley Greenery</title>
<link href="https://fonts.googleapis.com/css2?family=Source+Sans+3:wght@400;600;700&display=swap" rel="stylesheet">
<style>
:root{
  --blue:#0a74c4;
  --blue-dark:#065a9c;
  --blue-light:#1b8fe0;
  --green:#1f9a3a;
  --green-bright:#3cb043;
  --lime:#9ccc2e;
  --sky:#eef5fb;
  --text:#555;
  --link:#1166c4;
  --panel:#f2f2f2;
  --line:#d8d8d8;
  --footer:#2e2e2e;
  --footer-bar:#262626;
  --footer-text:#d8d8d8;
}
*{margin:0;padding:0;box-sizing:border-box}
html,body{width:952px;height:1200px;overflow:hidden}
body{font-family:"Source Sans 3",Arial,sans-serif;background:#fff;color:var(--text);position:relative}
a{text-decoration:none;color:inherit}

.site-header{position:absolute;left:0;top:0;width:952px;height:118px}
.brand{position:absolute;left:80px;top:42px;display:flex;align-items:center;gap:10px}
.brand-dot{width:30px;height:30px;border-radius:50%;background:var(--green-bright)}
.brand-name{font-size:24px;font-weight:700;color:var(--blue)}
.call{position:absolute;right:80px;top:14px;text-align:right}
.call-label{font-size:16px;color:var(--blue-light)}
.call-number{font-size:21px;font-weight:700;color:var(--green);line-height:1.1}
.search{position:absolute;left:713px;top:74px;width:159px;height:25px;border:1px solid #cfcfcf;font-size:11px;color:#444;padding:5px 11px}
.search svg{position:absolute;right:6px;top:5px}

.main-nav{position:absolute;left:0;top:118px;width:952px;height:37px;background:linear-gradient(var(--blue-light),var(--blue-dark));border-bottom:1px solid #04487c}
.main-nav ul{list-style:none;display:flex;position:absolute;left:80px;top:0;height:37px;border-right:1px solid rgba(0,0,0,.25)}
.main-nav li{height:37px;display:flex;align-items:center;justify-content:center;color:#fff;font-size:12.5px;font-weight:600;border-left:1px solid rgba(0,0,0,.25)}
.main-nav li.active{background:var(--green-bright)}

.hero{position:absolute;left:0;top:155px;width:952px;height:343px;background:var(--sky);border-bottom:1px solid #e2ebf2}
.hero-slide{position:absolute;left:79px;top:11px;width:794px;height:294px;background:linear-gradient(180deg,#c9b59a 0%,#8a9a6a 35%,#c7b7a0 65%,#5a8a3a 100%);box-shadow:0 10px 14px -8px rgba(0,0,0,.35)}
.hero-caption{position:absolute;left:0;right:0;bottom:22px;text-align:center;color:#fff;font-size:25px;font-weight:600;text-shadow:0 2px 3px rgba(0,0,0,.5)}
.hero-dots{position:absolute;left:442px;top:319px;display:flex;gap:8px}
.hero-dots span{width:11px;height:11px;border-radius:50%;background:#9a9a9a;box-shadow:inset 0 1px 2px rgba(0,0,0,.3)}
.hero-dots span.on{background:#6e6e6e}

.service{position:absolute;width:264px;text-align:center}
.service h2{font-size:18.5px;font-weight:600;color:var(--green);height:18px;line-height:18px}
.service-photo{display:block;margin-top:9px;width:264px;height:94px}
.service p{margin-top:11px;font-size:11.7px;line-height:18px;color:var(--text)}
.service p a{color:var(--link)}

.quick-contact{position:absolute;left:642px;top:537px;width:231px;height:347px;background:var(--panel);border:1px solid #e3e3e3}
.quick-contact h3{height:35px;background:linear-gradient(#48b848,#1f8d33);color:#fff;font-size:16.5px;font-weight:700;padding:7px 13px}
.field{position:absolute;left:11px;width:210px;height:30px;background:#fff;border:1px solid var(--line);font-size:10.5px;color:#666;padding:7px 11px}
.field.message{height:79px}
.submit{position:absolute;left:163px;top:308px;width:57px;height:26px;background:linear-gradient(#555,#2c2c2c);border-radius:3px;color:#fff;font-size:12px;font-weight:600;text-align:center;line-height:26px}

.site-footer{position:absolute;left:0;top:929px;width:952px;height:224px;background:var(--footer)}
.footer-col{position:absolute;top:33px}
.footer-col h4{font-size:14.5px;font-weight:400;color:var(--lime);margin-bottom:7px}
.footer-col ul{list-style:none}
.footer-col li{font-size:11.5px;line-height:20px;color:var(--footer-text)}
.social li{display:flex;align-items:center;gap:8px;line-height:26.5px;height:26.5px}
.social .icon{width:21px;height:21px;border-radius:50%;background:#fff}
.footer-brand{display:flex;align-items:center;gap:6px;margin-top:14px;padding-left:2px}
.footer-brand .dot{width:12px;height:12px;border-radius:50%;background:#8a8a8a}
.footer-brand span{font-size:10px;font-weight:700;color:#8a8a8a}
.footer-bar{position:absolute;left:0;top:1153px;width:952px;height:47px;background:var(--footer-bar);text-align:center;font-size:10.5px;color:#9a9a9a;line-height:47px}
</style>
</head>
<body>

<header class="site-header">
  <a class="brand" href="#"><span class="brand-dot"></span><span class="brand-name">Loxley Greenery</span></a>
  <div class="call">
    <div class="call-label">Call us Today</div>
    <div class="call-number">555 014 2387</div>
  </div>
  <div class="search">Search
    <svg width="13" height="13" viewBox="0 0 13 13"><circle cx="5" cy="5" r="3.6" fill="none" stroke="#222" stroke-width="1.8"/><line x1="7.6" y1="7.6" x2="12" y2="12" stroke="#222" stroke-width="2.2" stroke-linecap="round"/></svg>
  </div>
</header>

<nav class="main-nav">
  <ul>
    <li class="active" style="width:85px">HOME</li>
    <li style="width:106px">ABOUT US</li>
    <li style="width:99px">SERVICES</li>
    <li style="width:96px">GALLERY</li>
    <li style="width:127px">TESTIMONIALS</li>
    <li style="width:80px">NEWS</li>
    <li style="width:80px">BLOG</li>
    <li style="width:120px">CONTACT US</li>
  </ul>
</nav>

<section class="hero">
  <div class="hero-slide" role="img" aria-label="Desert garden patio with pool, palms, cacti and a shaded table at sunset">
    <div class="hero-caption">Morbi amet tortor ultricies justo egestas</div>
  </div>
  <div class="hero-dots"><span class="on"></span><span></span><span></span><span></span></div>
</section>

<article class="service" style="left:81px;top:536px">
  <h2>LANDSCAPING</h2>
  <div class="service-photo" role="img" aria-label="Landscaped pool surrounded by shrubs and flowers" style="background:linear-gradient(180deg,#6c8a3c,#3d7a8a 55%,#1d6ea0 75%,#c9a23a)"></div>
  <p>Interior Landscaping is the interior installation and maintenance of live plants and flowers.... <a href="#">More</a></p>
</article>
<article class="service" style="left:361px;top:536px">
  <h2>URBANSCAPING</h2>
  <div class="service-photo" role="img" aria-label="Stone path beside a koi pond with planted borders" style="background:linear-gradient(90deg,#8c8c80,#4a5a30 45%,#3a2a1a 60%,#7a9a3a)"></div>
  <p>Urbanscaping refers to landscaping in the urban environment and is restricted in this... <a href="#">More</a></p>
</article>
<article class="service" style="left:81px;top:727px">
  <h2>HOLIDAY DECORATING</h2>
  <div class="service-photo" role="img" aria-label="Raked gravel garden with a dark stone and moss" style="background:linear-gradient(120deg,#b8b2aa,#d4cfc8 50%,#9a968e 80%,#4a4a40)"></div>
  <p>Holiday Decorating is the Christmas/Hanukkah deco-rating during the winter.... <a href="#">More</a></p>
</article>
<article class="service" style="left:361px;top:727px">
  <h2>RENTAL PLANTS</h2>
  <div class="service-photo" role="img" aria-label="Nursery aisle lined with potted green plants" style="background:linear-gradient(180deg,#5a8a2a,#3a6a1a 50%,#9ab84a 80%,#b8b0a0)"></div>
  <p>Plant rentals is the short term rental of plants and live flowers (orchids, kalanchoe, etc) to event venues <a href="#">More</a></p>
</article>

<aside class="quick-contact">
  <h3>Quick Contact</h3>
  <div class="field" style="top:50px">Name</div>
  <div class="field" style="top:92px">Phone</div>
  <div class="field" style="top:133px">E-mail</div>
  <div class="field" style="top:175px">Postal Code</div>
  <div class="field message" style="top:216px">Message</div>
  <div class="submit">SUBMIT</div>
</aside>

<footer class="site-footer">
  <div class="footer-col" style="left:102px">
    <h4>Quick Links</h4>
    <ul><li>Home</li><li>About us</li><li>Services</li><li>Gallery</li><li>Testimonials</li><li>News</li><li>Blog</li></ul>
  </div>
  <div class="footer-col" style="left:246px">
    <h4>Support Links</h4>
    <ul><li>Press</li><li>Legal Notice</li><li>Privacy Policy</li><li>Term of Use</li><li>Help</li><li>Contact</li></ul>
  </div>
  <div class="footer-col" style="left:409px">
    <h4>Quick Links</h4>
    <ul><li>Home</li><li>About us</li><li>Services</li><li>Gallery</li><li>Testimonials</li><li>News</li><li>Blog</li></ul>
  </div>
  <div class="footer-col" style="left:548px">
    <h4>Support Links</h4>
    <ul><li>Press</li><li>Legal Notice</li><li>Privacy Policy</li><li>Term of Use</li><li>Help</li><li>Contact</li></ul>
  </div>
  <div class="footer-col" style="left:722px">
    <h4>Connect With Us</h4>
    <ul class="social">
      <li><span class="icon"></span>Friendwall</li>
      <li><span class="icon"></span>Chirper</li>
      <li><span class="icon"></span>Linkfolio</li>
    </ul>
    <div class="footer-brand"><span class="dot"></span><span>Loxley Greenery</span></div>
  </div>
</footer>
<div class="footer-bar">Copyright &copy; 2013 &nbsp;Loxley Greenery. &nbsp;All rights reserved.</div>

</body>
</html>
```